Memoir author looking for book cover design

Title:
"Tides, Thorns and Twilight"

Subtitle:
"The Journey to Reach my Brother, Vanished on the Glacier"

My book is about the 18-month-long search and grieving process after my husband went missing from a hiking accident.
See "notesbeyondthequietfjord.example" for background

(An "ampersand" may look best, but I'm unable to enter it in this format)

Reason: Having difficulty finishing up, in part due to time difference. Don't want designers to have to work in the middle of the night!

```html
<!DOCTYPE html>
<html lang="en">
<head>
<meta charset="utf-8">
<title>Tides, Thorns &amp; Twilight — Book Cover</title>
<link rel="stylesheet" href="https://fonts.googleapis.com/css2?family=Amatic+SC:wght@700&family=Arimo:wght@400;700&display=swap">
<style>
  :root {
    --sky-rust: #7a3a22;
    --sky-ember: #a8532c;
    --sun-glow: #f6d79a;
    --haze-gold: #d9a766;
    --mountain-moss: #6c7658;
    --forest-deep: #2c3424;
    --meadow-pale: #a9ad8c;
    --field-umber: #5e4a33;
    --field-dusk: #3a2f22;
    --ink-white: #fbf8f2;
    --band-shade: rgba(60, 40, 30, 0.45);
  }
  * { margin: 0; padding: 0; box-sizing: border-box; }
  html, body {
    width: 869px;
    height: 1200px;
    overflow: hidden;
    background: #ffffff;
  }
  .cover {
    position: relative;
    width: 869px;
    height: 1200px;
    overflow: hidden;
  }
  .cover-scene {
    position: absolute;
    inset: 0;
    background:
      radial-gradient(ellipse 420px 300px at 640px 380px, rgba(246,215,154,0.85), rgba(246,215,154,0) 70%),
      radial-gradient(ellipse 520px 260px at 120px 560px, rgba(217,167,102,0.55), rgba(217,167,102,0) 70%),
      radial-gradient(ellipse 600px 200px at 420px 980px, rgba(169,173,140,0.35), rgba(169,173,140,0) 70%),
      linear-gradient(180deg,
        var(--sky-rust) 0%,
        var(--sky-ember) 18%,
        var(--haze-gold) 34%,
        var(--mountain-moss) 48%,
        var(--forest-deep) 60%,
        var(--meadow-pale) 70%,
        var(--field-umber) 84%,
        var(--field-dusk) 100%);
  }
  .title {
    position: absolute;
    top: 8px;
    left: 40px;
    width: 720px;
    text-align: center;
    font-family: "Amatic SC", cursive;
    font-weight: 700;
    color: var(--ink-white);
    font-size: 150px;
    line-height: 168px;
    letter-spacing: 4px;
  }
  .subtitle {
    position: absolute;
    top: 478px;
    left: 178px;
    width: 508px;
    height: 72px;
    padding: 6px 12px;
    border-radius: 10px;
    background: var(--band-shade);
    color: var(--ink-white);
    font-family: "Arimo", Arial, sans-serif;
    font-size: 23px;
    line-height: 29px;
    text-align: center;
  }
  .subtitle strong { font-weight: 700; }
  .author {
    position: absolute;
    top: 858px;
    left: 430px;
    width: 380px;
    text-align: center;
    font-family: "Amatic SC", cursive;
    font-weight: 700;
    color: var(--ink-white);
    font-size: 84px;
    line-height: 90px;
    letter-spacing: 3px;
  }
</style>
</head>
<body>
  <main class="cover">
    <div class="cover-scene" role="img" aria-label="Photograph of a woman with red hair seen from behind, sitting in a meadow looking toward forested alpine slopes and mountains under a glowing sunset sky, framed by faint leaf sprigs in the corners"></div>
    <h1 class="title">Tides, Thorns<br>&amp; Twilight</h1>
    <p class="subtitle">The Journey to Reach my Brother,<br><strong>Vanished</strong> on the Glacier</p>
    <p class="author">Maren Lindqvist</p>
  </main>
</body>
</html>
```